Vonbrel Skincare 3D Bottle and Box

Hello, We need our label attach to the Tembo PUMP Top bottle. We need a 3 sided design-Front View, and 2 side views. We also want a clear side view of the PUMP TOP.
I also attach the label as a AI file

```html
<!DOCTYPE html>
<html lang="en">
<head>
<meta charset="utf-8">
<title>Vonbrel Skincare – Vitamin C Serum Pump Bottle</title>
<link rel="stylesheet" href="https://fonts.googleapis.com/css2?family=Raleway:wght@300;400;500&family=Roboto:wght@400;500&display=swap">
<style>
  :root {
    --page-top: #e9e9e9;
    --page-bottom: #fafafa;
    --label: #ffffff;
    --orange: #f39a1e;
    --orange-deep: #ee7a10;
    --orange-light: #f9b24c;
    --gold: #f1c84e;
    --ink: #444444;
    --ink-soft: #6f6f6f;
    --rule: #8a8a8a;
  }
  * { box-sizing: border-box; margin: 0; padding: 0; }
  html, body { width: 900px; height: 1200px; overflow: hidden; }
  body {
    background: linear-gradient(180deg, var(--page-top) 0%, var(--page-bottom) 70%, #ffffff 100%);
    font-family: "Raleway", sans-serif;
    color: var(--ink);
    position: relative;
  }
  .bottle-art { position: absolute; left: 0; top: 0; width: 900px; height: 1200px; }

  .label {
    position: absolute;
    left: 270px; top: 609px;
    width: 363px; height: 434px;
    overflow: hidden;
  }
  .label__side {
    position: absolute; top: 24px;
    width: 90px;
    font-family: "Roboto", sans-serif;
    font-size: 6.5px; line-height: 1.9;
    color: var(--ink-soft);
  }
  .label__side--left { left: -74px; text-align: right; }
  .label__side--right { left: 346px; }
  .label__side p + p { margin-top: 8px; }

  .brand {
    position: absolute; left: 18px; top: 56px;
    color: #fff; font-weight: 300; line-height: 1;
  }
  .brand__name { display: block; font-size: 72px; letter-spacing: -0.5px; }
  .brand__sub { display: block; font-size: 28px; text-align: right; margin-top: 2px; }

  .product { position: absolute; left: 0; right: 0; top: 204px; text-align: center; }
  .product__name { font-size: 36px; font-weight: 400; letter-spacing: 1.5px; line-height: 1; color: var(--ink); }
  .product__type { font-size: 25px; font-weight: 400; letter-spacing: 1.5px; line-height: 1; margin-top: 10px; color: var(--ink); }
  .product__tag {
    display: inline-block; margin-top: 9px; padding: 2px 4px;
    font-family: "Roboto", sans-serif;
    font-size: 8.5px; color: var(--ink-soft);
    border-top: 1px solid var(--rule); border-bottom: 1px solid var(--rule);
  }
  .actives {
    list-style: none;
    margin: 48px auto 0; width: 168px;
    font-family: "Roboto", sans-serif;
    font-size: 13px; color: var(--ink);
  }
  .actives li { padding: 2px 0 3px; border-top: 1px solid var(--rule); line-height: 1.2; }

  .volume {
    position: absolute; left: 0; right: 0; top: 434px;
    text-align: center;
    color: #fff; font-family: "Roboto", sans-serif; font-weight: 500;
    font-size: 19px; letter-spacing: 0.5px;
  }
</style>
</head>
<body>
  <svg class="bottle-art" viewBox="0 0 900 1200" aria-hidden="true">
    <defs>
      <linearGradient id="amber" x1="0" y1="0" x2="1" y2="0">
        <stop offset="0" stop-color="#b54f06"/>
        <stop offset="0.18" stop-color="#e27b14"/>
        <stop offset="0.5" stop-color="#f5a23a"/>
        <stop offset="0.82" stop-color="#e27b14"/>
        <stop offset="1" stop-color="#b54f06"/>
      </linearGradient>
      <linearGradient id="amberBase" x1="0" y1="0" x2="0" y2="1">
        <stop offset="0" stop-color="#e06a10"/>
        <stop offset="1" stop-color="#9c2f06"/>
      </linearGradient>
      <linearGradient id="pump" x1="0" y1="0" x2="1" y2="0">
        <stop offset="0" stop-color="#0c0c0c"/>
        <stop offset="0.35" stop-color="#2e2e2e"/>
        <stop offset="0.6" stop-color="#1a1a1a"/>
        <stop offset="1" stop-color="#060606"/>
      </linearGradient>
      <linearGradient id="waveFill" x1="0" y1="0" x2="0" y2="1">
        <stop offset="0" stop-color="#f6a63a"/>
        <stop offset="1" stop-color="#f39a1e"/>
      </linearGradient>
      <linearGradient id="band" x1="0" y1="0" x2="0" y2="1">
        <stop offset="0" stop-color="#f39a1e"/>
        <stop offset="1" stop-color="#ec7410"/>
      </linearGradient>
      <radialGradient id="shadow" cx="0.5" cy="0.5" r="0.5">
        <stop offset="0" stop-color="#000" stop-opacity="0.22"/>
        <stop offset="1" stop-color="#000" stop-opacity="0"/>
      </radialGradient>
    </defs>

    <ellipse cx="452" cy="1172" rx="210" ry="16" fill="url(#shadow)"/>

    <!-- amber bottle body -->
    <path d="M357 440 H551 V505 C551 528 633 532 633 585 V1138 Q633 1172 598 1172 H305 Q270 1172 270 1138 V585 C270 532 357 528 357 505 Z" fill="url(#amber)"/>
    <rect x="270" y="1078" width="363" height="94" rx="30" fill="url(#amberBase)"/>
    <rect x="420" y="450" width="8" height="150" fill="#ffd08a" opacity="0.35"/>
    <rect x="478" y="450" width="6" height="150" fill="#7a3004" opacity="0.35"/>

    <!-- label base -->
    <rect x="270" y="609" width="363" height="434" fill="#ffffff"/>
    <path d="M270 609 H633 V766 C590 760 545 772 490 786 C420 804 350 806 270 788 Z" fill="url(#waveFill)"/>
    <path d="M270 788 C350 806 420 804 490 786 C545 772 590 760 633 766 V774 C590 768 545 780 490 794 C420 812 350 814 270 797 Z" fill="#f9c06a"/>
    <rect x="270" y="1022" width="363" height="5" fill="var(--gold)"/>
    <rect x="270" y="1027" width="363" height="52" fill="url(#band)"/>
    <rect x="270" y="609" width="22" height="470" fill="#000" opacity="0.06"/>
    <rect x="611" y="609" width="22" height="470" fill="#000" opacity="0.06"/>
    <circle cx="617" cy="941" r="10" fill="none" stroke="#8a8a8a" stroke-width="1.2"/>

    <!-- pump top -->
    <rect x="334" y="252" width="234" height="193" rx="4" fill="url(#pump)"/>
    <rect x="334" y="252" width="234" height="10" fill="#000" opacity="0.5"/>
    <rect x="377" y="129" width="156" height="124" rx="3" fill="url(#pump)"/>
    <rect x="404" y="56" width="76" height="76" rx="4" fill="url(#pump)"/>
    <rect x="438" y="66" width="14" height="9" rx="2" fill="#d8d8d8"/>
  </svg>

  <section class="label" aria-label="Vonbrel Skincare Vitamin C Serum label">
    <div class="label__side label__side--left">
      <p>Apply two to three drops on clean skin morning and night. Follow with moisturizer and sunscreen. Keep away from eyes.</p>
    </div>
    <div class="label__side label__side--right">
      <p>Ingredients: Aqua, Sodium Ascorbyl Phosphate, Aloe Leaf Juice, Hyaluronic Acid, Jojoba Oil, Tocopherol, Glycerin, Ferulic Acid, Witch Hazel Extract, Phenoxyethanol.</p>
      <p>Store cool and dry.</p>
    </div>

    <div class="brand">
      <span class="brand__name">Vonbrel</span>
      <span class="brand__sub">skincare</span>
    </div>

    <div class="product">
      <h1 class="product__name">VITAMIN C</h1>
      <h2 class="product__type">SERUM</h2>
      <p class="product__tag">Advanced Anti Aging Formula</p>
      <ul class="actives">
        <li>25% Vitamin C</li>
        <li>Hyaluronic Acid</li>
        <li>Jojoba Oil + Vitamin E</li>
      </ul>
    </div>
  </section>
  <p class="volume" style="top:1040px">1 FL OZ / 30 ML</p>
</body>
</html>
```